Mezzanine Floor Manufacturer looking for a new business card design

We manufacture mezzanine floors and are providers of racking systems. We provide a range of items/services - simple rack repairs , full warehouse fit outs , manufacturer and install mezzanine floors , partitioning and large turnkey projects. Recently had a new website - www.corvane-shelving.co.uk and would like our business cards updating aswell . Our current card is single sided in the old logo colours (pdf attached) and needs updating.

Target Market(s)

We deal with large projects/ multi national companies and also smaller projects and companies throughout the UK ranging from a single warehouse to a large multi site company.

Industry/Entity Type

Business

Contact Information for Business Card

Will have job title,tel no's, email ,website address etc like example pdf

Requirements
Must have
• Hi - needs to use the colours of the logo & new website. Card needs to be professional

```html
<!DOCTYPE html>
<html lang="en">
<head>
<meta charset="utf-8">
<title>Corvane Shelving Ltd – Business Card</title>
<link href="https://fonts.googleapis.com/css2?family=Open+Sans:wght@400;600;700;800&display=swap" rel="stylesheet">
<style>
  :root{
    --brand-red:#c8202a;
    --ink:#5a5a5a;
    --card:#ffffff;
    --backdrop:#e6e6e6;
  }
  *{margin:0;padding:0;box-sizing:border-box}
  html,body{width:1200px;height:780px;overflow:hidden}
  body{
    background:var(--backdrop);
    font-family:"Open Sans",Arial,sans-serif;
    color:var(--ink);
    position:relative;
  }
  .card{
    position:absolute;top:216px;width:540px;height:348px;
    background:var(--card);overflow:hidden;
    box-shadow:0 6px 18px rgba(0,0,0,.18);
  }
  .card--services{left:30px}
  .card--contact{left:630px}

  .brand-mark{
    position:absolute;display:flex;align-items:center;gap:8px;
    font-weight:800;color:var(--brand-red);
  }
  .brand-mark__dot{display:block;border-radius:50%;background:var(--brand-red)}
  .card--services .brand-mark{top:30px;right:34px;font-size:22px}
  .card--services .brand-mark__dot{width:18px;height:18px}
  .company-name{position:absolute;font-weight:800;color:var(--brand-red);letter-spacing:.2px}
  .card--services .company-name{top:78px;left:36px;font-size:26px}
  .services-title{
    position:absolute;top:124px;left:56px;
    font-size:20px;font-weight:400;color:var(--brand-red);
  }
  .services-list{
    position:absolute;top:154px;left:58px;list-style:none;
    font-size:14px;line-height:20px;color:var(--ink);
  }
  .services-list li{position:relative;padding-left:16px}
  .services-list li::before{
    content:"";position:absolute;left:0;top:8px;width:5px;height:5px;
    border-radius:50%;background:var(--brand-red);
  }
  .address{font-size:14px;line-height:19px;color:var(--ink)}
  .card--services .address{position:absolute;top:256px;left:74px}
  .website{color:var(--brand-red);font-size:14px}

  .wave{position:absolute;inset:0}
  .person{position:absolute;top:44px;right:28px;text-align:right;color:#fff}
  .person__name{font-size:18px;font-weight:700;letter-spacing:.5px;white-space:nowrap}
  .person__role{font-size:11px;letter-spacing:1px;opacity:.8}
  .card--contact .brand-mark{top:186px;left:36px;font-size:24px}
  .card--contact .brand-mark__dot{width:20px;height:20px}
  .card--contact .company-name{top:220px;left:36px;font-size:22px}
  .contact-list{
    position:absolute;top:260px;left:36px;list-style:none;
    font-size:14px;line-height:20px;color:var(--ink);
  }
  .contact-list li{display:flex;align-items:center;gap:8px}
  .contact-list svg{width:12px;height:12px;fill:var(--brand-red);flex:none}
  .card--contact .address{
    position:absolute;top:190px;right:30px;font-size:13px;line-height:18px;
  }
  .card--contact .website{position:absolute;top:254px;right:30px;color:var(--ink);font-size:13px}
</style>
</head>
<body>

<section class="card card--services">
  <div class="brand-mark"><span class="brand-mark__dot"></span>Corvane</div>
  <h2 class="company-name">Corvane Shelving Ltd</h2>
  <h3 class="services-title">Services</h3>
  <ul class="services-list">
    <li>simple rack repairs</li>
    <li>full warehouse fit outs</li>
    <li>manufacturer and install mezzanine floors</li>
    <li>partitioning and large turnkey projects</li>
  </ul>
  <p class="address">Twelve Mill Lane<br>Ashbrook Business Park Heanor<br>Derbyshire DE7 4QT<br><span class="website">www.corvane-shelving.co.uk</span></p>
</section>

<section class="card card--contact">
  <svg class="wave" viewBox="0 0 540 348" aria-hidden="true">
    <path d="M0 118 C160 100 260 40 340 0 L540 0 L540 82 C460 112 420 150 330 166 C220 186 100 180 0 176 Z" fill="var(--brand-red)"/>
  </svg>
  <div class="person">
    <div class="person__name">DALEN WHITCOMBE</div>
    <div class="person__role">TECHNICAL SALES</div>
  </div>
  <div class="brand-mark"><span class="brand-mark__dot"></span>Corvane</div>
  <h2 class="company-name">Corvane Shelving Ltd</h2>
  <ul class="contact-list">
    <li><svg viewBox="0 0 12 12"><rect x="3" y="0" width="6" height="12" rx="1"/></svg>07700 900418</li>
    <li><svg viewBox="0 0 12 12"><path d="M1 4 Q6 0 11 4 L9 6 L8 4 L4 4 L3 6 Z M3 7 L9 7 L10 12 L2 12 Z"/></svg>01632 960512</li>
    <li><svg viewBox="0 0 12 12"><rect x="3" y="0" width="6" height="4"/><rect x="0" y="4" width="12" height="6" rx="1"/></svg>01632 960731</li>
    <li><svg viewBox="0 0 12 12"><path d="M0 2 L12 2 L12 10 L0 10 Z M0 2 L6 7 L12 2" stroke="#fff" stroke-width=".8"/></svg>sales@corvane-shelving.co.uk</li>
  </ul>
  <p class="address">Twelve Mill Lane<br>Ashbrook Business Park Heanor<br>Derbyshire DE7 4QT</p>
  <p class="website">www.corvane-shelving.co.uk</p>
</section>

</body>
</html>
```